Accounting firm needing business card / letterhead designed
Marcus T. Elbering, CPA
marcus@fernquill.com
www.fernquill.com
482 N Harlow Ave Alder Bend, OH 43719
419-555-0172

```html
<!DOCTYPE html>
<html lang="en">
<head>
<meta charset="utf-8">
<title>Fernquill Business Card</title>
<link rel="stylesheet" href="https://fonts.googleapis.com/css2?family=Source+Sans+3:wght@400;600;700&display=swap">
<style>
  :root {
    --canvas-bg: #2b2b2e;
    --brand-green: #8dc63f;
    --brand-navy: #2b2a6e;
    --card-white: #ffffff;
    --text-on-dark: #ffffff;
  }
  * { box-sizing: border-box; margin: 0; padding: 0; }
  html, body {
    width: 1200px;
    height: 900px;
    overflow: hidden;
    background: var(--canvas-bg);
    font-family: "Source Sans 3", Arial, sans-serif;
  }
  .canvas {
    width: 1200px;
    height: 900px;
    display: flex;
    flex-direction: column;
    align-items: center;
    justify-content: center;
    gap: 56px;
  }
  .card {
    position: relative;
    width: 660px;
    height: 378px;
    overflow: hidden;
    box-shadow: 0 14px 30px rgba(0, 0, 0, 0.45);
  }

  /* Front side */
  .card-front {
    background: var(--brand-green);
    color: var(--text-on-dark);
  }
  .card-front .brand-name {
    position: absolute;
    left: 0; right: 0;
    top: 138px;
    text-align: center;
    font-size: 68px;
    font-weight: 700;
    letter-spacing: 8px;
    color: var(--text-on-dark);
  }
  .card-front .website {
    position: absolute;
    left: 0; right: 0;
    bottom: 44px;
    text-align: center;
    font-size: 15px;
    letter-spacing: 6px;
  }

  /* Back side */
  .card-back {
    background: var(--card-white);
  }
  .card-back .band {
    position: absolute;
    inset: 0;
  }
  .card-back .brand-name {
    position: absolute;
    left: 0; right: 0;
    top: 84px;
    text-align: center;
    font-size: 58px;
    font-weight: 700;
    letter-spacing: 7px;
    color: var(--brand-navy);
  }
  .contact {
    position: absolute;
    left: 40px;
    width: 560px;
    top: 252px;
    text-align: center;
    color: var(--text-on-dark);
    font-size: 15px;
    line-height: 1.45;
  }
  .contact .person {
    font-weight: 700;
    font-size: 17px;
  }
  .contact .web {
    letter-spacing: 3px;
  }
</style>
</head>
<body>
  <main class="canvas">
    <section class="card card-front">
      <div class="brand-name">FERNQUILL</div>
      <div class="website">www.fernquill.com</div>
    </section>

    <section class="card card-back">
      <svg class="band" width="660" height="378" viewBox="0 0 660 378" aria-hidden="true">
        <path d="M0,236 L360,236 C480,236 570,205 660,130 L660,378 L0,378 Z" fill="var(--brand-navy)"/>
        <path d="M0,228 L360,228 C480,228 570,197 660,122" fill="none" stroke="var(--brand-green)" stroke-width="4"/>
      </svg>
      <div class="brand-name">FERNQUILL</div>
      <div class="contact">
        <p class="person">Marcus T. Elbering, CPA</p>
        <p>482 N Harlow Ave, Alder Bend, OH 43719</p>
        <p>P: 555-201-0172 &nbsp;E: marcus@fernquill.com</p>
        <p class="web">www.fernquill.com</p>
      </div>
    </section>
  </main>
</body>
</html>
```